Velno Recycling needs a new web design

We need a new web design for our company based in Austin, TX. We resell and recycling electronics such as laptops, computer components, Tovlets, Brunos, etc. Since our inception over ten years ago, we’ve become one of the premier electronics recycling and remarketing companies in Austin, Texas.

```html
<!DOCTYPE html>
<html lang="en">
<head>
<meta charset="utf-8">
<title>Velno Recycling</title>
<link rel="stylesheet" href="https://fonts.googleapis.com/css2?family=Open+Sans:wght@400;600;700&display=swap">
<style>
  :root {
    --frame: #e6e6e6;
    --page: #ffffff;
    --navy: #2b2b50;
    --blue: #1b72c0;
    --text: #4a4a4a;
    --rule: #cfcfcf;
    --hero-dark: #2c2e33;
    --hero-mid: #7d7f84;
    --hero-copper: #b5622a;
  }
  * { margin: 0; padding: 0; box-sizing: border-box; }
  html, body {
    width: 1191px; height: 1200px; overflow: hidden;
    background: var(--frame);
    font-family: "Open Sans", Arial, sans-serif;
  }
  .page {
    position: absolute; left: 15px; top: 15px;
    width: 1161px; height: 1170px;
    background: var(--page);
  }
  .site-header { position: relative; height: 127px; }
  .brand {
    position: absolute; left: 20px; top: 38px;
    display: flex; align-items: center; gap: 12px;
  }
  .brand-mark {
    width: 62px; height: 62px; border-radius: 50%;
    background: var(--blue);
  }
  .brand-name {
    font-size: 30px; font-weight: 700; color: var(--blue);
    letter-spacing: 0.5px;
  }
  .main-nav {
    position: absolute; right: 56px; top: 60px;
    display: flex; align-items: center; gap: 20px;
  }
  .main-nav a {
    font-size: 14.5px; font-weight: 700; color: #1e1e1e;
    text-decoration: none; text-transform: uppercase;
  }
  .main-nav a.is-active { border-bottom: 3px solid var(--navy); padding-bottom: 3px; margin-top: 6px; }
  .main-nav a.nav-cta {
    background: var(--blue); color: #fff; border-radius: 3px;
    padding: 7px 14px;
  }
  .hero {
    position: absolute; left: 0; top: 127px; width: 1161px; height: 564px;
    background:
      radial-gradient(circle at 25% 40%, rgba(181,98,42,0.55), transparent 30%),
      radial-gradient(circle at 70% 60%, rgba(181,98,42,0.5), transparent 28%),
      radial-gradient(circle at 50% 20%, rgba(200,200,205,0.5), transparent 35%),
      linear-gradient(135deg, var(--hero-mid), var(--hero-dark) 55%, var(--hero-mid));
    clip-path: polygon(0 0, 100% 0, 100% 486px, 50% 564px, 0 486px);
  }
  .intro {
    position: absolute; left: 0; top: 735px; width: 1161px; text-align: center;
  }
  .intro-title {
    display: inline-flex; align-items: center; gap: 22px;
    font-size: 24px; font-weight: 700; color: var(--navy); letter-spacing: 0.5px;
  }
  .intro-title::before, .intro-title::after {
    content: ""; width: 95px; height: 1px; background: var(--rule);
  }
  .intro-copy {
    margin: 30px auto 0; width: 1010px;
    font-size: 13.4px; line-height: 19.5px; color: var(--text);
  }
  .site-footer {
    position: absolute; left: 0; top: 1121px; width: 1161px;
    border-top: 1px solid #555; padding-top: 14px; text-align: center;
    font-size: 11px; font-weight: 700; color: #333;
  }
</style>
</head>
<body>
<div class="page">
  <header class="site-header">
    <div class="brand">
      <span class="brand-mark"></span>
      <span class="brand-name">Velno Recycling</span>
    </div>
    <nav class="main-nav">
      <a href="#" class="is-active">Home</a>
      <a href="#">About</a>
      <a href="#">Services</a>
      <a href="#">News</a>
      <a href="#" class="nav-cta">Contact Us</a>
    </nav>
  </header>

  <div class="hero" role="img" aria-label="Photograph of a pile of salvaged electronic components, optical drive parts with copper ribbon cables"></div>

  <section class="intro">
    <h1 class="intro-title">VELNO RECYCLING</h1>
    <p class="intro-copy">Lorem ipsum dolor sit amet, consectetuer adipiscing elit, sed diam nonummy nibh euismod tincidunt ut laoreet dolore magna aliquam erat volutpat. Ut wisi enim ad minim veniam, quis nostrud exerci tation ullamcorper suscipit lobortis nisl ut aliquip ex ea commodo consequat. Duis autem vel eum iriure dolor in hendrerit in vulputate velit esse molestie consequat, vel illum dolore eu feugiat nulla facilisis at vero eros et accumsan et iusto odio dignissim qui blandit praesent luptatum zzril delenit augue duis dolore te feugait nulla facilisi. Nam liber tempor cum soluta nobis eleifend option congue nihil imperdiet doming id quod mazim placerat facer possim assum. Typi non habent claritatem insitam; est usus legentis in iis qui facit eorum claritatem. Investigationes demonstraverunt lectores legere me lius quod ii legunt saepius.</p>
  </section>

  <footer class="site-footer">© 2018 VELNO RECYCLING I ALL RIGHTS RESERVED</footer>
</div>
</body>
</html>
```